Large logo design on utility truck.

Would like my logo to be placed on both sides of the vehicle large enough to be read from 20 metres away. Am open to a design that includes the bonnet area but not compulsory. Am open to stripes, shapes or any other designs. Please use the two blue colours in my logo. Some black and/or white is possible too maybe. Please design for only the front cabin area of the truck (silver painted area) not the rear tray area or toolbox. I don't really have any predesigned ideas. I will communicate regularly. Please supply final files in vector format.

Target Market(s)

Women home owners 30-60yrs

Industry/Entity Type

Home Improvement

Font styles to use
Sans Serif

Colors
0555a3
0692cd

Requirements
Must have
• Veranda Forge Logo
Nice to have
• bright and clean design. easily seen from a distance.
I've added some images of security mesh for reference only - not to be used. nice to work some mesh in.
Should not have
• Please remove the word 'THE' from the logo, so its 'VERANDA FORGE'

```html
<!DOCTYPE html>
<html lang="en">
<head>
<meta charset="utf-8">
<title>Veranda Forge – Vehicle Side Graphics</title>
<link rel="stylesheet" href="https://fonts.googleapis.com/css2?family=Montserrat:wght@600;700;800&display=swap">
<style>
  :root {
    --brand-blue: #0555a3;
    --bright-blue: #0692cd;
    --navy: #0b2f86;
    --panel: #eef0f2;
    --page: #ffffff;
    --white: #ffffff;
  }
  html, body {
    margin: 0;
    padding: 0;
    width: 1200px;
    height: 1200px;
    overflow: hidden;
    background: var(--page);
    font-family: "Montserrat", Arial, sans-serif;
  }
  .canvas {
    position: relative;
    width: 1200px;
    height: 1200px;
  }
  .side-graphic {
    position: absolute;
    left: 50px;
    width: 1100px;
    height: 440px;
    background: var(--panel);
    overflow: hidden;
  }
  .side-graphic--passenger { top: 110px; }
  .side-graphic--driver { top: 650px; }

  .web-address {
    position: absolute;
    top: 40px;
    font-size: 24px;
    font-weight: 700;
    letter-spacing: 0.5px;
    color: var(--navy);
  }
  .web-address__domain { color: var(--brand-blue); }

  .brand-name {
    position: absolute;
    top: 92px;
    margin: 0;
    font-size: 86px;
    font-weight: 700;
    line-height: 0.95;
    color: var(--brand-blue);
    text-align: right;
    letter-spacing: -1px;
  }
  .brand-square {
    position: absolute;
    top: 60px;
    width: 170px;
    height: 170px;
    background: var(--brand-blue);
  }

  .band {
    position: absolute;
    left: 0;
    right: 0;
    top: 290px;
    height: 80px;
    background: var(--navy);
  }
  .stripe {
    position: absolute;
    left: 0;
    right: 0;
    top: 370px;
    height: 24px;
    background: var(--bright-blue);
  }
  .phone {
    position: absolute;
    top: 300px;
    font-size: 50px;
    font-weight: 700;
    color: var(--white);
    letter-spacing: 1px;
  }

  /* layout positions per side */
  .side-graphic--passenger .web-address { left: 110px; }
  .side-graphic--passenger .brand-name { right: 360px; }
  .side-graphic--passenger .brand-square { left: 760px; }
  .side-graphic--passenger .phone { left: 130px; }

  .side-graphic--driver .web-address { left: 60px; }
  .side-graphic--driver .brand-name { right: 420px; }
  .side-graphic--driver .brand-square { left: 700px; }
  .side-graphic--driver .phone { left: 80px; }
</style>
</head>
<body>
<main class="canvas">

  <section class="side-graphic side-graphic--passenger" aria-label="Passenger side cabin graphic">
    <div class="band"></div>
    <div class="stripe"></div>
    <div class="web-address">www.<span class="web-address__domain">verandaforge</span>.com</div>
    <h1 class="brand-name">VERANDA<br>FORGE</h1>
    <div class="brand-square"></div>
    <div class="phone">555-014-7261</div>
  </section>

  <section class="side-graphic side-graphic--driver" aria-label="Driver side cabin graphic">
    <div class="band"></div>
    <div class="stripe"></div>
    <div class="web-address">www.<span class="web-address__domain">verandaforge</span>.com</div>
    <h2 class="brand-name">VERANDA<br>FORGE</h2>
    <div class="brand-square"></div>
    <div class="phone">555-014-7261</div>
  </section>

</main>
</body>
</html>
```